Prairie Civic Builders Summit (PCBS) needs a flyer and logo design

We need a save the date flyer that can be easily edited to be a header only with event title, date and location.
We also are looking for a conference logo that will go well with our company logo.
Updates
Most of you are submitting an agenda design. Not a graphic flyer design. This isn't what I'm needing. I need something that can easily be a save the date with a header and is graphically appealing. Additionally, I've only gotten 2 logo designs.
Target Market(s)
Architects, engineers, public owners, contractors, attorneys
Industry/Entity Type
Construction
Logo Text
Prairie Civic Builder's Summit
Requirements
Must have
- Flyer should Have:
- Title: "The Lantern across Quiet Meadows - Project Delivery to Operations”
- Date: August 8-9, 2019
- Location: Fort Worth, TX
- One-page only
- Conference Logo should be relatable to our company logo: Prairie Civic Builders Summit.
Nice to have
- Topics:
- Alternative Constrcting: JOC & Design-Build
- Dealing with Contracting in a Tight TX Industry
- Tools & Technologies Project Delivery and Operations: Design and Construction
- Tools & Technologies: Coordinating Operations
Should not have
- Detailed agenda

```html
<!DOCTYPE html>
<html lang="en">
<head>
<meta charset="utf-8">
<title>Save the Date – Prairie Civic Builders Summit</title>
<link rel="stylesheet" href="https://fonts.googleapis.com/css2?family=Audiowide&family=Montserrat:wght@400;600;700;800&display=swap">
<style>
  :root{
    --backdrop:#1f2021;
    --paper:#ffffff;
    --brand-blue:#2f4ea0;
    --ink:#2a2a2a;
    --slate:#4b4b4b;
    --leaf:#8cb23f;
    --rule:rgba(255,255,255,.85);
    --water-light:#dbe4f3;
    --water-mid:#a9bde3;
    --water-deep:#6f8ccc;
  }
  *{box-sizing:border-box;margin:0;padding:0}
  html,body{width:927px;height:1200px;overflow:hidden;background:var(--backdrop)}
  body{position:relative;font-family:"Montserrat",sans-serif}
  .flyer{position:absolute;left:67px;top:87px;width:794px;height:1026px;background:var(--paper);overflow:hidden}
  .org-mark{position:absolute;left:24px;top:36px;display:flex;align-items:center;gap:10px}
  .org-mark .dot{width:50px;height:50px;border-radius:50%;background:var(--brand-blue)}
  .org-mark .name{font-weight:700;font-size:22px;color:var(--brand-blue)}
  .summit-mark{position:absolute;left:0;right:0;top:108px;display:flex;justify-content:center;align-items:center;gap:8px}
  .summit-mark .dot{width:40px;height:40px;border-radius:50%;background:var(--brand-blue)}
  .summit-mark .name{font-weight:800;font-size:16px;line-height:1.05;color:var(--brand-blue);width:190px}
  .headline{position:absolute;left:0;right:0;top:162px;padding-left:8px;text-align:center;font-family:"Audiowide",sans-serif;font-weight:400;color:var(--brand-blue);font-size:112px;line-height:96px;letter-spacing:8px;-webkit-text-stroke:2px var(--brand-blue)}
  .event-box{position:absolute;left:105px;top:353px;width:583px;height:220px;background:var(--leaf)}
  .event-date{text-align:center;font-family:"Audiowide",sans-serif;color:#fff;font-size:44px;line-height:52px;letter-spacing:2px;margin-top:4px;-webkit-text-stroke:1px #fff}
  .event-place{text-align:center;font-family:"Audiowide",sans-serif;color:#fff;font-size:20px;letter-spacing:2px;margin-top:-4px}
  .sessions{position:absolute;left:16px;right:10px;top:86px;display:flex}
  .day{color:var(--ink)}
  .day-thu{width:259px;padding-right:10px}
  .day-fri{flex:1;border-left:1px solid var(--rule);padding-left:22px}
  .day-title{font-weight:800;font-size:12.5px}
  .day-mc{font-size:12.5px;margin-bottom:8px}
  .topic{border-top:1px solid var(--rule);padding-top:5px;margin-bottom:7px;width:100px;white-space:nowrap}
  .topic-label{font-weight:800;font-size:8px}
  .topic-text{font-weight:700;font-size:9px;line-height:1.3}
  .theme{position:absolute;left:0;right:0;top:590px;text-align:center;font-family:"Audiowide",sans-serif;letter-spacing:1.5px}
  .theme-main{color:var(--brand-blue);font-size:28.5px;-webkit-text-stroke:.8px var(--brand-blue)}
  .theme-sub{color:var(--slate);font-size:29px;margin-top:-2px;-webkit-text-stroke:.8px var(--slate)}
  .scene{position:absolute;left:0;right:0;bottom:0;height:370px;background:linear-gradient(180deg,rgba(255,255,255,0) 0%,var(--water-light) 22%,var(--water-mid) 60%,var(--water-deep) 78%,var(--water-light) 100%)}
</style>
</head>
<body>
  <main class="flyer">
    <div class="org-mark"><span class="dot"></span><span class="name">Larkspan Institute</span></div>
    <div class="summit-mark"><span class="dot"></span><span class="name">PRAIRIE CIVIC BUILDERS SUMMIT</span></div>
    <h1 class="headline">SAVE<br>THE DATE</h1>
    <section class="event-box">
      <p class="event-date">AUGUST 8–9, 2019</p>
      <p class="event-place">FT. WORTH, TEXAS</p>
      <div class="sessions">
        <div class="day day-thu">
          <p class="day-title">THURSDAY, Aug. 8:</p>
          <p class="day-mc">(Marcus Bell MC)</p>
          <div class="topic"><p class="topic-label">TOPIC 1:</p><p class="topic-text">Alternative Contracting:<br>JOC and Design-Build Deliveries</p></div>
          <div class="topic"><p class="topic-label">TOPIC 2:</p><p class="topic-text">Dealing with Contracting in a Tight Texas Industry</p></div>
        </div>
        <div class="day day-fri">
          <p class="day-title">FRIDAY, Aug. 9:</p>
          <p class="day-mc">(Joan Whitfield MC)</p>
          <div class="topic"><p class="topic-label">TOPIC 3A:</p><p class="topic-text">Tools and Technologies from Project Delivery<br>into Operations - Design and Construction Technologies</p></div>
          <div class="topic"><p class="topic-label">TOPIC 3B:</p><p class="topic-text">Tools and Technologies from Project Delivery<br>into Operations - Coordinating Operations</p></div>
        </div>
      </div>
    </section>
    <div class="theme">
      <p class="theme-main">THE LANTERN ACROSS QUIET MEADOWS</p>
      <p class="theme-sub">PROJECT DELIVERY TO OPERATIONS</p>
    </div>
    <div class="scene" role="img" aria-label="Blue sketch-style illustration of a steel truss bridge spanning a river with trees on the far bank"></div>
  </main>
</body>
</html>
```